Night Dresses business cards business requirers

We are a new company initiating Mexico operations. Our core business is Night woman dress (both formal and party dress) for rent. Gownhaven is the name of the company. ITS Gownhaven form by two word. The dress word and topia (Utopic) so the place Gownhaven Means That You cant get the ideal, perfect and unique dress for your event. So we would like a modern, very creative, and attractive business card.

Industry/Entity Type

Womens Clothing

Contact Information for Business Card

Rounded Borders, two faces

Requirements
Must have
• Rounded borders, logo and slogan, modern, glam, attractive design
Should not have
• modern design classic or not

```html
<!DOCTYPE html>
<html lang="en">
<head>
<meta charset="utf-8">
<title>Gownhaven Business Cards</title>
<link rel="stylesheet" href="https://fonts.googleapis.com/css2?family=Montserrat:wght@400;500;700&family=Open+Sans:wght@400;600&display=swap">
<style>
  :root {
    --orchid: #b86496;
    --orchid-line: #d7a9c4;
    --paper: #ffffff;
    --ink: #4a4a4a;
    --ink-soft: #5c5c5c;
    --stage: #e9e6e8;
  }
  * { box-sizing: border-box; margin: 0; padding: 0; }
  html, body { width: 1200px; height: 1200px; overflow: hidden; }
  body {
    background: var(--stage);
    font-family: "Open Sans", Arial, sans-serif;
    display: flex;
    flex-direction: column;
    align-items: center;
    justify-content: center;
    gap: 60px;
  }
  .card {
    width: 840px;
    height: 480px;
    border-radius: 56px;
    position: relative;
    box-shadow: 0 10px 30px rgba(0,0,0,0.12);
  }
  /* Front face */
  .card--front {
    background: var(--paper);
    padding: 14px;
  }
  .card--front .face {
    width: 100%;
    height: 100%;
    background: var(--orchid);
    border-radius: 46px;
    display: flex;
    align-items: center;
    justify-content: center;
  }
  .company { text-align: center; }
  .company__name {
    font-family: "Montserrat", Arial, sans-serif;
    font-weight: 500;
    font-size: 44px;
    letter-spacing: 2px;
  }
  .company__slogan {
    font-family: "Open Sans", Arial, sans-serif;
    font-weight: 400;
    font-size: 18px;
    margin-top: 6px;
  }
  .card--front .company { color: var(--paper); }

  /* Back face */
  .card--back {
    background: var(--orchid);
    padding: 18px;
  }
  .card--back .face {
    width: 100%;
    height: 100%;
    background: var(--paper);
    border-radius: 42px;
    display: flex;
    align-items: center;
    padding: 0 50px 0 60px;
  }
  .brand-block {
    width: 370px;
    display: flex;
    flex-direction: column;
    align-items: center;
    gap: 20px;
  }
  .brand-block__dot {
    width: 80px;
    height: 80px;
    border-radius: 50%;
    border: 4px solid var(--orchid);
  }
  .card--back .company { color: var(--ink); }
  .card--back .company__name { font-size: 36px; }
  .card--back .company__slogan { font-size: 16px; }

  .divider {
    width: 1.5px;
    height: 260px;
    background: var(--orchid-line);
    margin: 0 30px 0 20px;
  }
  .contact { color: var(--ink-soft); }
  .contact__name {
    font-family: "Montserrat", Arial, sans-serif;
    font-weight: 700;
    font-size: 30px;
    color: var(--orchid);
  }
  .contact__role { font-size: 16px; margin: 2px 0 22px 8px; }
  .contact__list { list-style: none; font-size: 17px; line-height: 1.6; }
  .contact__list li { display: flex; align-items: flex-start; gap: 12px; }
  .contact__list svg { width: 16px; height: 16px; fill: var(--orchid); margin-top: 6px; flex: none; }
  .contact__list .address { margin-top: 12px; }
</style>
</head>
<body>
  <section class="card card--front" aria-label="Business card front">
    <div class="face">
      <div class="company">
        <div class="company__name">Gownhaven</div>
        <div class="company__slogan">Evening gowns to borrow</div>
      </div>
    </div>
  </section>

  <section class="card card--back" aria-label="Business card back">
    <div class="face">
      <div class="brand-block">
        <div class="brand-block__dot"></div>
        <div class="company">
          <div class="company__name">Gownhaven</div>
          <div class="company__slogan">Evening gowns to borrow</div>
        </div>
      </div>
      <div class="divider"></div>
      <div class="contact">
        <div class="contact__name">JOHN DOE</div>
        <div class="contact__role">Director</div>
        <ul class="contact__list">
          <li>
            <svg viewBox="0 0 16 16"><path d="M2 6c0-2 3-3 6-3s6 1 6 3v1h-3V6H5v1H2zM4 8h8l1 5H3z"/></svg>
            <span>1-234-567890</span>
          </li>
          <li>
            <svg viewBox="0 0 16 16"><circle cx="8" cy="8" r="7"/><path d="M1 8h14M8 1c3 3 3 11 0 14M8 1c-3 3-3 11 0 14" stroke="#fff" stroke-width="1.2" fill="none"/></svg>
            <span>www.gownhaven-rent.com</span>
          </li>
          <li>
            <svg viewBox="0 0 16 16"><path d="M1 3h14v10H1z"/><path d="M1 3l7 6 7-6" stroke="#fff" stroke-width="1.2" fill="none"/></svg>
            <span>john@gownhaven-rent.com</span>
          </li>
          <li class="address">
            <svg viewBox="0 0 16 16"><path d="M8 1l7 7h-2v7H9v-4H7v4H3V8H1z"/></svg>
            <span>Dummy city<br>Dummy Country Land</span>
          </li>
        </ul>
      </div>
    </div>
  </section>
</body>
</html>
```